Microsite for a private healthcare provider

The design I need (PSD file) is for a company offering two services:
1. Recruitment of nurses
2. Provider a private health care: prenatal classes, vaccines for travellers
Here's a website we designed and we would like a similar style in terms of layout. Please note there will be about the same amount of content (text) http://lumivexstudio.ca/fr
Main menu with 4 sections:
Accueil |Agence de placement | Soins privés | Contact
Links to their social media accounts:
https://twitter.com/SoinsBrevalo
https://www.facebook.com/pages/SoinsBrevalo-Agence-de-placement-en-soins-de-sant%C3%A9/482913057264135
Contact details:
TÉL. (450) 555-0143
TÉLEC. (450) 555-0198
7186 boulevard Perrault, suite 1400
St-Hubert (Québec), J4X 1K3
Target Market(s)
Nurses looking for a job, Expecting women, People about to travel and seeking vaccines
Industry/Entity Type
Healthcare
Requirements
Must have
- 1- Must be responsive for mobiles and tablets
2 - Chirplo feed
3 - Google maps at the end next to their contact details
4- Two contact forms:
Form for people to send in their resume.
The form title is: Postulez
Fields required:
Nom complet
Courriel
Téléphone
Années d'expérience (with drop down list: 1-2 ans, 3-5 ans, 5 ans et plus)
Choose file (possibility to attach a cv)
Message
Form for requesting information
Form title is: Demande d'informations
Fields are:
Nom complet
Téléphone
Courriel
Message
Nice to have
- Here are some images on Pixtura Foto the client likes, you can use for inspiration.
Agence de placement section:
File #40718253
File #6381947
File #5124086
File #8057291
File #30961472
File #27430685
File #45816037
Soins privés section:
File #36274519
File #49102853
File #31687240
File #25049716
File #43705128
File #38519602
File #29873154
File #7260835
File #34918657

```html
<!DOCTYPE html>
<html lang="fr">
<head>
<meta charset="utf-8">
<title>SoinsBrevalo — Soins de santé personnalisés</title>
<link rel="stylesheet" href="https://fonts.googleapis.com/css2?family=Didact+Gothic&family=Arimo:wght@400;700&display=swap">
<style>
:root{
  --navy-deep:#06203f;
  --navy:#0b3565;
  --navy-light:#14548f;
  --link-blue:#1f7fe0;
  --brand-green:#8cbd2c;
  --field-bg:#ececec;
  --field-border:#8d8d8d;
  --ink:#1b1b1b;
  --white:#ffffff;
  --band-light:#f4f4f4;
  --band-dark:#b9b9b9;
}
*{box-sizing:border-box;margin:0;padding:0}
html,body{width:900px;height:1200px;overflow:hidden}
body{position:relative;background:var(--white);font-family:"Didact Gothic",sans-serif;color:var(--ink)}

/* Header */
.site-header{position:absolute;left:0;top:0;width:900px;height:340px;
  background:radial-gradient(ellipse at 50% 45%,var(--navy-light) 0%,var(--navy) 45%,var(--navy-deep) 100%)}
.brand{position:absolute;left:68px;top:0;width:298px;height:62px;background:var(--white);
  border:2px solid #d5d5d5;padding:6px 10px}
.brand-name{font-family:"Arimo",sans-serif;font-weight:700;font-size:30px;line-height:32px;color:var(--navy-light);display:flex;align-items:center;gap:8px}
.brand-name .dot{width:10px;height:10px;background:var(--brand-green);display:inline-block}
.brand-tagline{font-size:11px;color:#2f6b1e;margin-top:4px}
.utility{position:absolute;left:639px;top:18px;width:176px;font-size:11px;color:var(--white)}
.utility .links{display:flex;justify-content:space-between;padding:0 2px 0 6px}
.search{margin-top:3px;height:16px;background:linear-gradient(#f0f0f0,#c9c9c9);position:relative}
.search svg{position:absolute;right:3px;top:1px}

.main-nav{position:absolute;left:150px;top:62px;width:660px;height:80px;display:flex}
.main-nav a{flex:1;display:flex;flex-direction:column;align-items:center;justify-content:flex-start;
  color:var(--white);text-decoration:none;font-size:18px;letter-spacing:1px;line-height:15px;text-align:center;
  background:linear-gradient(rgba(255,255,255,.12),rgba(255,255,255,.02));border-right:2px solid rgba(0,0,0,.35);padding-top:12px}
.main-nav a:last-child{border-right:none}
.main-nav svg{margin-bottom:10px}

.hero-text{position:absolute;left:166px;top:209px;color:var(--white);font-size:19px;letter-spacing:1.5px;line-height:26px;text-shadow:0 0 .6px #fff,0 0 .6px #fff}
.hero-text span{display:block;padding-left:48px}
.hero-arrow{position:absolute;top:222px}
.hero-visual{position:absolute;left:500px;top:136px;width:240px;height:196px;border-radius:50% 50% 20px 20px;
  background:radial-gradient(circle at 55% 40%,#e9eef4 0%,#9fb9d6 45%,rgba(20,84,143,0) 75%)}

/* Welcome band */
.welcome{position:absolute;left:0;top:340px;width:900px;height:82px;
  background:linear-gradient(var(--band-light) 0%,#e3e3e3 55%,var(--band-dark) 100%)}
.welcome h1{position:absolute;left:214px;top:1px;font-family:"Arimo",sans-serif;font-size:23px;font-weight:700;letter-spacing:1px}
.welcome h1 .brand-inline{font-family:"Didact Gothic",sans-serif;font-weight:400;color:var(--navy-light)}
.welcome p{position:absolute;left:200px;top:28px;width:640px;font-size:11.5px;line-height:15.5px;letter-spacing:.35px;text-indent:14px}

/* Offers */
.offer{position:absolute;top:454px;width:230px;height:164px;border:1px solid #333;border-bottom:none;
  box-shadow:0 2px 4px rgba(0,0,0,.25)}
.offer h2{margin:5px 14px 0;height:24px;background:linear-gradient(90deg,var(--navy-deep),var(--navy-light),var(--navy-deep));
  color:var(--white);font-family:"Arimo",sans-serif;font-size:14px;font-weight:700;text-align:center;line-height:24px}
.offer p{margin:10px 10px 0;font-size:10px;line-height:11.6px;text-align:center;letter-spacing:.2px}
.offer a{position:absolute;right:8px;bottom:2px;color:var(--link-blue);font-size:16px;text-decoration:none;letter-spacing:1px}

/* Application form */
.apply-title{position:absolute;left:103px;top:705px;font-size:22px;font-weight:400;display:flex;align-items:center;gap:8px}
.field-label{position:absolute;width:170px;left:10px;text-align:right;font-size:12.5px;letter-spacing:.3px}
.field{position:absolute;left:192px;height:17px;background:var(--field-bg);border-top:1px solid var(--field-border);border-left:1px solid #bbb}
.select{font-size:11px;color:#555;padding-left:10px;line-height:17px;display:flex;justify-content:space-between;padding-right:4px}
.file-btn{position:absolute;left:312px;top:846px;width:64px;height:11px;background:var(--navy-deep);color:#cfd8e4;font-size:7px;text-align:center;line-height:11px}
.btn-blue{position:absolute;background:linear-gradient(#3a8cf0,#0f52c5);color:var(--white);border-radius:6px;text-align:center;
  box-shadow:0 2px 3px rgba(0,0,0,.35)}

.divider{position:absolute;left:630px;top:640px;width:4px;height:385px;background:linear-gradient(90deg,#ddd,#f7f7f7);
  box-shadow:-14px 0 18px rgba(0,0,0,.08)}

/* Info request */
.info-title{position:absolute;left:660px;top:655px;width:214px;text-align:center;font-size:15px;font-weight:400;line-height:11px;letter-spacing:.5px}
.side-label{position:absolute;left:662px;font-size:12px;letter-spacing:.3px;color:var(--navy)}
.side-field{position:absolute;left:657px;width:225px;height:17px;background:var(--field-bg);border-top:1px solid var(--field-border)}
.dotted{position:absolute;left:655px;top:863px;width:230px;border-top:2px dotted #555}

.newsletter{position:absolute;left:675px;top:896px;width:202px;height:114px;background:#dcdcdc;box-shadow:0 2px 6px rgba(0,0,0,.4)}
.newsletter h3{height:28px;background:linear-gradient(var(--navy-light),var(--navy-deep));color:var(--white);
  font-weight:400;font-size:17px;letter-spacing:1px;line-height:28px;padding-left:23px}
.newsletter p{font-size:10px;margin:10px 0 0 5px}
.newsletter .email{margin:2px 3px 0 3px;height:20px;background:var(--white);color:#aaa;font-size:13px;padding-left:30px;line-height:20px}
.newsletter .signup{margin:11px 0 0 25px;width:149px;height:20px;border-radius:10px;background:linear-gradient(#f5f5f5,#bdbdbd);
  border:1px solid #888;text-align:center;font-size:14px;line-height:18px;font-weight:700;font-family:"Arimo",sans-serif}

/* Footer */
.site-footer{position:absolute;left:0;top:1043px;width:900px;height:157px;
  background:radial-gradient(ellipse at 50% 20%,var(--navy-light) 0%,var(--navy) 50%,var(--navy-deep) 100%);color:var(--white)}
.footer-bar{height:45px;background:rgba(0,0,0,.3);display:flex}
.footer-bar h4{font-weight:400;font-size:15px;letter-spacing:1.2px;line-height:52px;padding-left:30px;border-right:2px solid rgba(0,0,0,.4)}
.social{position:absolute;left:52px;top:61px;list-style:none;font-size:12px;line-height:17.5px;letter-spacing:.6px}
.social li::before{content:"";display:inline-block;border-left:7px solid #cfd8e4;border-top:4px solid transparent;border-bottom:4px solid transparent;margin-right:8px}
.support{position:absolute;left:232px;top:60px;width:390px;font-size:10px;line-height:12px;letter-spacing:.2px;text-indent:22px}
.contact{position:absolute;left:638px;top:64px;font-size:12px;line-height:12px;letter-spacing:.4px;font-style:normal}
.copyright{position:absolute;left:0;top:139px;width:900px;text-align:center;font-size:11.5px;letter-spacing:.7px}
</style>
</head>
<body>

<header class="site-header">
  <div class="brand">
    <div class="brand-name"><span>SoinsBrevalo</span><span class="dot"></span></div>
    <div class="brand-tagline">Soins de santé personnalisés, en privé</div>
  </div>

  <div class="utility">
    <div class="links"><span>Site Map</span><span>User area</span></div>
    <div class="search">
      <svg width="14" height="14" viewBox="0 0 14 14"><circle cx="8" cy="5.5" r="4" fill="none" stroke="#111" stroke-width="1.6"/><line x1="5" y1="8.5" x2="1" y2="12.5" stroke="#111" stroke-width="2"/></svg>
    </div>
  </div>

  <nav class="main-nav">
    <a href="#"><svg width="34" height="24" viewBox="0 0 34 24"><path d="M3 12 L17 2 L31 12" fill="none" stroke="#fff" stroke-width="3"/><rect x="7" y="11" width="20" height="12" fill="#fff"/><rect x="11" y="14" width="4" height="4" fill="#335"/><rect x="19" y="14" width="4" height="4" fill="#335"/></svg>Accueil</a>
    <a href="#"><svg width="20" height="26" viewBox="0 0 20 26"><circle cx="10" cy="5" r="5" fill="#fff"/><rect x="3" y="11" width="14" height="15" rx="4" fill="#fff"/></svg>Agence de<br>placement</a>
    <a href="#"><svg width="20" height="26" viewBox="0 0 20 26"><circle cx="10" cy="5" r="5" fill="#fff"/><rect x="3" y="11" width="14" height="15" rx="4" fill="#fff"/></svg><span style="margin-top:6px">Soins privés</span></a>
    <a href="#"><svg width="36" height="24" viewBox="0 0 36 24"><rect x="1" y="4" width="34" height="18" fill="none" stroke="#fff" stroke-width="2"/><path d="M1 4 L18 15 L35 4" fill="none" stroke="#fff" stroke-width="2"/></svg>Contact</a>
  </nav>

  <p class="hero-text">Votre entreprise a besoin<span>d'idées fraîches fraîches</span></p>
  <svg class="hero-arrow" style="left:106px" width="36" height="28" viewBox="0 0 36 28"><path d="M36 2 L2 14 L36 26 L24 14 Z" fill="#0a1b30"/></svg>
  <svg class="hero-arrow" style="left:752px" width="36" height="28" viewBox="0 0 36 28"><path d="M0 2 L34 14 L0 26 L12 14 Z" fill="#0a1b30"/></svg>
  <div class="hero-visual" role="img" aria-label="Illustration d'une infirmière avec une seringue"></div>
</header>

<section class="welcome">
  <h1>Bienvenu a <span class="brand-inline">SoinsBrevalo</span> !</h1>
  <p>Lorem ipsum dolor sit amet, consectetur adipiscing elit. Nunc iaculis sagittis accumsan. Phasellus nibh erat, tristique ut lobortis sed, varius non eros. Praesent aliquam lacus pharetra turpis laoreet volutpat.</p>
</section>

<article class="offer" style="left:73px">
  <h2>Offer #1</h2>
  <p>Lorem ipsum dolor sit amet, consectetur adipiscing elit. Cras ut mi enim, ac iaculis leo. Duis imperdiet dolor sed quam aliquet eleifend consequat ipsum egestas. Duis non dui nulla. Praesent quis eros sed sapien gravida hendrerit. In sem dui, placerat id tempor quis, aliquam quis magna.</p>
  <a href="#">En savoir plus…</a>
</article>
<article class="offer" style="left:340px">
  <h2>Offer #2</h2>
  <p>Lorem ipsum dolor sit amet, consectetur adipiscing elit. Cras ut mi enim, ac iaculis leo. Duis imperdiet dolor sed quam aliquet eleifend consequat ipsum egestas. Duis non dui nulla. Praesent quis eros sed sapien gravida hendrerit. In sem dui, placerat id tempor quis, aliquam quis magna.</p>
  <a href="#">En savoir plus…</a>
</article>
<article class="offer" style="left:604px">
  <h2>Offer #3</h2>
  <p>Lorem ipsum dolor sit amet, consectetur adipiscing elit. Cras ut mi enim, ac iaculis leo. Duis imperdiet dolor sed quam aliquet eleifend consequat ipsum egestas. Duis non dui nulla. Praesent quis eros sed sapien gravida hendrerit. In sem dui, placerat id tempor quis, aliquam quis magna.</p>
  <a href="#">En savoir plus…</a>
</article>

<section class="apply-form">
  <h2 class="apply-title">
    <svg width="22" height="22" viewBox="0 0 22 22"><path d="M4 2 L14 2 L12 8 L17 12 L5 12 Z" fill="#1d6fd6" transform="rotate(-35 11 8)"/><line x1="8" y1="12" x2="18" y2="21" stroke="#0b3565" stroke-width="2"/></svg>
    Postulez
  </h2>
  <span class="field-label" style="top:740px">Nom Complet</span><div class="field" style="top:739px;width:260px"></div>
  <span class="field-label" style="top:764px">Courriel</span><div class="field" style="top:763px;width:260px"></div>
  <span class="field-label" style="top:789px">Téléphone</span><div class="field" style="top:790px;width:175px"></div>
  <span class="field-label" style="top:817px">Années d'expérience</span>
  <div class="field select" style="top:817px;width:113px"><span>1 - 2 ans</span><svg width="10" height="10" viewBox="0 0 10 10" style="margin-top:4px"><path d="M0 1 L10 1 L5 8 Z" fill="#111"/></svg></div>
  <span class="field-label" style="top:844px">Attach CV</span><div class="field" style="top:843px;width:113px"></div>
  <span class="file-btn">Choose File</span>
  <span class="field-label" style="top:870px">Message</span><div class="field" style="top:871px;width:389px;height:80px"></div>
  <div class="btn-blue" style="left:284px;top:973px;width:181px;height:38px;font-size:21px;line-height:38px;letter-spacing:1px">Envoyer</div>
</section>

<div class="divider"></div>

<section class="info-form">
  <h2 class="info-title">Demande<br>d'informations</h2>
  <span class="side-label" style="top:683px">Nom complet</span><div class="side-field" style="top:698px"></div>
  <span class="side-label" style="top:719px">Téléphone</span><div class="side-field" style="top:735px"></div>
  <span class="side-label" style="top:757px">Courriel</span><div class="side-field" style="top:774px"></div>
  <span class="side-label" style="top:796px">Message</span><div class="side-field" style="top:812px"></div>
  <div class="btn-blue" style="left:706px;top:835px;width:118px;height:26px;font-size:15px;line-height:26px;letter-spacing:.5px">Envoyer</div>
  <div class="dotted"></div>
</section>

<aside class="newsletter">
  <h3>Newsletter</h3>
  <p>Sign up for weekly newsletter</p>
  <div class="email">E-mail</div>
  <div class="signup">Sign-Up</div>
</aside>

<footer class="site-footer">
  <div class="footer-bar">
    <h4 style="width:227px">Social Networks</h4>
    <h4 style="width:398px;padding-left:35px">Quick Solutions and Support</h4>
    <h4 style="border:none;padding-left:12px">Contact us!</h4>
  </div>
  <ul class="social">
    <li>Chirplo</li>
    <li>Amicircle</li>
    <li>Cerclepost</li>
  </ul>
  <p class="support">Lorem ipsum dolor sit amet, consectetur adipiscing elit. Cras ut mi enim, ac iaculis leo.<br>&nbsp;&nbsp;&nbsp;&nbsp;&nbsp;Duis imperdiet dolor sed quam aliquet eleifend consequat ipsum egestas.</p>
  <address class="contact">TÉL. (450) 555-0143<br>TÉLEC. (450) 555-0198<br>7186 boulevard Perrault, suite 1400<br>St-Hubert (Québec), J4X 1K3</address>
  <p class="copyright">Copyright 2013 SoinsBrevalo. All rights reserved !</p>
</footer>

</body>
</html>
```